Business card design needed

I am a nutritionist and fitness instructor and I need a business card designed for my company SowGrowThrive. I provide nutrition education services such as consultations, cooking demonstrations, workshops, and supermarket tours. I also provide fitness instruction and training to clients to help overhaul their lifestyle.

I would like to see designs that have a natural, organic, feel using earthy colours. I would like to have cards printed on recycled paper.

I would prefer a 2 sided card. Front side with just the business name Sow Grow Thrive and underneath Nutrition Health Fitness. The second side to have the contact details.

The final design should communicate health and wellness through eating organic wholefoods and being physically active.

Although I have this idea, I would be open to see other suggestions that have a similar look and feel.
Updates

Target Market(s)

people interested in being healthier, women wanting to loose weight, mothers wanting to be healthier for their families

Industry/Entity Type

Nutrition

Contact Information for Business Card

Nadia Crewe
Nutritionist and Personal Trainer
M 0417582936
E sowgrowthrivenutrition@mailbox-example.net

Logo Text

SowGrowThrive (underneath) Nutrition Health Fitness

Logo styles of interest
Wordmark Logo
Requirements
Nice to have
• I like the idea of having the letters of SowGrowThrive spelt out with food such as grains, nuts, seeds, legumes, fruit etc. For example close up images of cherry tomatoes, chia seeds, kidney beans, chickpeas, blue berries, raspberries, brown rice - lots of different colours and textures. Continuing playing on the idea of the book cover Dig Rest Glow.

food is important - I am not selling supplements rather I am promoting the enjoyment of healthy wholefoods so food is important to the look and feel of the design
Should not have
• cartoon images
images associated with body building or supplements
fruit or dumb bells with tape measures around them
clichés for weight loss such as scales and tape measures
I don't want to look like other typical wellness services such as massage or spa services

```html
<!DOCTYPE html>
<html lang="en">
<head>
<meta charset="utf-8">
<title>Nadia Crewe — Business Card</title>
<link rel="stylesheet" href="https://fonts.googleapis.com/css2?family=Playball&family=Marcellus&family=Didact+Gothic&display=swap">
<style>
  :root {
    --page: #ffffff;
    --card: #dedeb3;
    --ink: #3a2e12;
  }
  html, body {
    margin: 0;
    padding: 0;
    width: 1200px;
    height: 693px;
    overflow: hidden;
    background: var(--page);
  }
  .card {
    position: absolute;
    left: 46px;
    top: 46px;
    width: 1107px;
    height: 602px;
    background: var(--card);
    color: var(--ink);
  }
  .card__name {
    position: absolute;
    left: 76px;
    top: 320px;
    margin: 0;
    font-family: "Playball", cursive;
    font-weight: 400;
    font-size: 84px;
    line-height: 1;
    color: var(--ink);
    -webkit-text-stroke: 0.6px var(--ink);
  }
  .card__details {
    position: absolute;
    left: 229px;
    top: 438px;
    margin: 0;
  }
  .card__role {
    margin: 0 0 8px;
    font-family: "Marcellus", serif;
    font-size: 25px;
    letter-spacing: 0.14em;
    text-transform: uppercase;
    line-height: 1.2;
  }
  .card__contact {
    margin: 0;
    font-family: "Didact Gothic", sans-serif;
    font-size: 25px;
    line-height: 38px;
  }
</style>
</head>
<body>
  <main class="card">
    <h1 class="card__name">Nadia Crewe</h1>
    <div class="card__details">
      <p class="card__role">Nutritionist and Personal Trainer</p>
      <p class="card__contact">M 0417582936 E<br>sowgrowthrivenutrition@mailbox-example.net</p>
    </div>
  </main>
</body>
</html>
```